Email Signature and a letter head

I need a professional email signature and a letter head for letters sent by post. I've attached my logo and a signature i am currently using. Current letter head is also attached.

Target Market(s)

Accounting Clients

Industry/Entity Type

Public Accounting

Font styles to use
Sans Serif

Colors

Designer to choose colors to be used in the design.

Requirements
Must have
• My logo, RJ Logo, Plumo Logo, Tax Agent logo. All attached.
• All my credentials - examples in the attached documents

```html
<!DOCTYPE html>
<html lang="en">
<head>
<meta charset="utf-8">
<title>Summit to Shore Business Services – Letterhead</title>
<link href="https://fonts.googleapis.com/css2?family=Open+Sans:wght@400;600;700&display=swap" rel="stylesheet">
<style>
  :root {
    --navy: #0b1526;
    --gold: #c9992a;
    --gold-deep: #a2822a;
    --paper: #f3f3f3;
    --paper-shade: #e6e6e6;
    --backdrop: #d9d9d9;
    --ink-light: #ffffff;
    --ink-muted: #4a4f5a;
    --badge-grey: #c9c9c9;
    --watermark: #e7e2d8;
  }
  * { margin: 0; padding: 0; box-sizing: border-box; }
  html, body { width: 1200px; height: 780px; overflow: hidden; }
  body {
    background: var(--backdrop);
    font-family: "Open Sans", Arial, sans-serif;
    position: relative;
  }
  .letterhead {
    position: absolute;
    left: 332px;
    top: 11px;
    width: 595px;
    height: 842px;
    transform: scale(0.9);
    transform-origin: top left;
    background: linear-gradient(160deg, var(--paper) 40%, var(--paper-shade) 100%);
    overflow: hidden;
  }
  .header-wave { position: absolute; left: 0; top: 0; width: 595px; height: 140px; }
  .brand {
    position: absolute;
    left: 50px;
    top: 22px;
    width: 134px;
    text-align: center;
    color: var(--gold);
    font-weight: 600;
  }
  .brand-mark {
    width: 50px; height: 50px;
    margin: 0 auto 6px;
    border: 2px solid var(--gold);
    border-radius: 50%;
  }
  .brand-name { font-size: 11.5px; letter-spacing: 0.4px; line-height: 1.1; white-space: nowrap; }
  .brand-sub { font-size: 5.5px; letter-spacing: 1.6px; text-transform: uppercase; }
  .contact {
    position: absolute;
    left: 366px;
    top: 20px;
    color: var(--ink-light);
    font-size: 7.6px;
    line-height: 11px;
  }
  .contact-name { color: var(--gold); font-weight: 700; font-size: 9.6px; margin-bottom: 1px; }
  .contact-line { display: flex; align-items: center; gap: 4px; white-space: nowrap; }
  .contact-line svg { width: 7px; height: 7px; flex: none; }
  .credentials {
    position: absolute;
    left: 380px;
    top: 112px;
    display: flex;
    align-items: center;
    gap: 16px;
  }
  .cred {
    display: flex;
    align-items: center;
    gap: 4px;
    color: var(--ink-muted);
    font-weight: 600;
    font-size: 9px;
  }
  .cred .shape { width: 22px; height: 22px; border-radius: 50%; background: var(--badge-grey); flex: none; }
  .cred-tax { font-size: 4.5px; line-height: 1.2; font-weight: 600; }
  .watermark {
    position: absolute;
    left: 99px;
    top: 273px;
    width: 406px;
    height: 406px;
    border: 5px solid var(--watermark);
    border-radius: 50%;
    display: flex;
    align-items: center;
    justify-content: center;
    color: var(--watermark);
    font-weight: 600;
    font-size: 34px;
    text-align: center;
    line-height: 1.15;
  }
  .footer-band {
    position: absolute;
    left: 0; bottom: 0;
    width: 100%; height: 16px;
    background: var(--gold-deep);
  }
</style>
</head>
<body>
  <main class="letterhead">
    <svg class="header-wave" viewBox="0 0 595 140" aria-hidden="true">
      <path d="M0,0 H595 V128 C570,116 530,106 480,104 C400,100 300,120 200,130 C120,138 60,136 0,124 Z" fill="var(--gold)"/>
      <path d="M0,0 H595 V112 C570,104 530,97 480,96 C400,94 300,116 200,126 C120,134 60,132 0,120 Z" fill="var(--navy)"/>
    </svg>

    <div class="brand">
      <div class="brand-mark"></div>
      <div class="brand-name">Summit to Shore</div>
      <div class="brand-sub">Business Services</div>
    </div>

    <div class="contact">
      <div class="contact-name">Marlee Foster RJ BBus.</div>
      <div class="contact-line">
        <svg viewBox="0 0 10 10"><path d="M5 0.5a3.2 3.2 0 0 0-3.2 3.2C1.8 6 5 9.5 5 9.5S8.2 6 8.2 3.7A3.2 3.2 0 0 0 5 .5zm0 4.4a1.2 1.2 0 1 1 0-2.4 1.2 1.2 0 0 1 0 2.4z" fill="var(--gold)"/></svg>
        18 Harbour Lane, Seacliff North VIC 3100
      </div>
      <div class="contact-line">
        <svg viewBox="0 0 10 10"><path d="M2.2 0.8l1.6 1.8-1 1.2c.6 1.4 1.8 2.6 3.2 3.2l1.2-1 1.8 1.6-.9 1.5C4.4 8.9 1.1 5.6.7 1.7z" fill="var(--gold)"/></svg>
        0412345678
      </div>
      <div class="contact-line">
        <svg viewBox="0 0 10 10"><rect x="0.5" y="2" width="9" height="6" fill="var(--gold)"/><path d="M0.5 2L5 5.5 9.5 2" stroke="var(--navy)" stroke-width="0.9" fill="none"/></svg>
        marlee@summittoshorebusiness.com.au
      </div>
      <div class="contact-line">
        <svg viewBox="0 0 10 10"><circle cx="5" cy="5" r="4.2" fill="none" stroke="var(--gold)" stroke-width="1.1"/><path d="M0.8 5h8.4M5 0.8c-2 2.4-2 6 0 8.4M5 0.8c2 2.4 2 6 0 8.4" stroke="var(--gold)" stroke-width="0.8" fill="none"/></svg>
        www.summittoshorebusiness.com.au
      </div>
      <div class="contact-line">ABN: 12 345 678 901 | TAN: 987 654 32</div>
    </div>

    <div class="credentials">
      <div class="cred cred-rj">RJ</div>
      <div class="cred cred-plumo">Plumo<span class="shape"></span></div>
      <div class="cred cred-tax"><span class="shape"></span><span>Tax agent<br>87654321</span></div>
    </div>

    <div class="watermark">Summit to<br>Shore</div>

    <div class="footer-band"></div>
  </main>
</body>
</html>
```